Brisk Tide needs a web page for E-commerce site

Small startup business looking for a custom website for my New Saltwater apparel Co.

COMPANY OVERVIEW

Brisk Tide was founded In Mont Belvieu, Tx, right on the heart of pelham cove.

Brisk Tide is the adrenaline, sweat pumping moment you find yourself setting the hook on a monster fish. This is the moment when all your senses come to life as you work to land that trophy, and after a grueling fight when your hi-fiving your fishing buddies...It's that moment... when the waters and the air around you are Brisk Sweet....All or Nothing...pure Addiction......This is BRISK TIDE

Looking for a sharp clean sexy web page for my ecommerce page

I like the look of black background websites.

www.brisktide-demo.com
Updates

I am using shopvane as my host site if that means anything to y'all

Thank you all for the submissions! There were some great ones!  I will have more projects in the future. thanks again

Target Market(s)

inshore/offshore fishing, saltwater enthusiast

Industry/Entity Type

Business

Requirements
Must have
• logo's

inshore/offshore fishing appeal

compatible with shopvane site

```html
<!DOCTYPE html>
<html lang="en">
<head>
<meta charset="utf-8">
<title>Brisk Tide — Saltwater Apparel</title>
<link href="https://fonts.googleapis.com/css2?family=Noto+Serif:wght@400;700&family=Open+Sans:wght@400;600;700&display=swap" rel="stylesheet">
<style>
  :root {
    --black: #000;
    --bar-top: #3d3d3d;
    --bar-bottom: #1f1f1f;
    --hero-band: #1b1b1b;
    --line: #3a3a3a;
    --white: #fff;
    --text-light: #f2f2f2;
    --price-bg: #ececec;
    --ink: #1a1a1a;
    --green: #19b187;
    --green-dark: #0f8d6a;
    --green-deep: #0d5f49;
    --btn-light: #ececec;
    --water: #8f9682;
    --water-dark: #59624f;
    --jacket: #6b716e;
    --tee-dark: #2a2218;
    --teal: #1c9c96;
  }
  * { box-sizing: border-box; margin: 0; padding: 0; }
  html, body { width: 1113px; height: 1200px; overflow: hidden; background: var(--black); }
  .page {
    position: relative; width: 1100px; height: 1186px;
    transform: scale(1.0118); transform-origin: 0 0;
    font-family: "Open Sans", sans-serif; color: var(--text-light);
  }
  .abs { position: absolute; white-space: nowrap; }

  .util-bar {
    left: 0; top: 0; width: 1100px; height: 46px;
    background: linear-gradient(var(--bar-top), var(--bar-bottom));
    border-bottom: 1px solid #444;
  }
  .util-nav {
    right: 89px; top: 13px; font-size: 13px; font-weight: 700; letter-spacing: .2px;
    color: var(--white);
  }
  .util-nav span { margin: 0 9px; }

  .brand {
    left: 95px; top: 80px; font-family: "Noto Serif", serif; font-weight: 700;
    font-size: 44px; color: var(--white); letter-spacing: 1px; line-height: 1;
  }
  .cart {
    left: 863px; top: 50px; width: 150px; height: 35px; border: 1px solid #555;
    background: #111; font-size: 13px; font-weight: 600; color: var(--white);
    display: flex; align-items: center; padding-left: 8px; gap: 10px;
  }
  .main-nav {
    left: 559px; top: 109px; height: 46px; display: flex;
    border: 1px solid var(--line); border-bottom: none;
  }
  .main-nav a {
    font-family: "Noto Serif", serif; font-size: 16px; letter-spacing: .5px;
    color: var(--white); text-decoration: none; padding-top: 13px; text-align: center;
    border-right: 1px solid var(--line);
  }
  .main-nav a:nth-child(1), .main-nav a:nth-child(2) { width: 108px; }
  .main-nav a:nth-child(3) { width: 144px; border-right: none; }
  .checkout {
    left: 934px; top: 114px; width: 95px; height: 34px; background: var(--btn-light);
    border: 1px solid #bbb; font-family: "Noto Serif", serif; font-size: 14px; color: #333;
    display: flex; align-items: center; justify-content: center;
  }

  .hero-band {
    left: 0; top: 155px; width: 1100px; height: 407px; background: var(--hero-band);
    border-top: 1px solid var(--line); border-bottom: 1px solid var(--line);
  }
  .hero-photo {
    left: 86px; top: 172px; width: 937px; height: 348px; border: 1px solid var(--white);
    background: linear-gradient(90deg, var(--water-dark) 0%, var(--water) 25%, var(--jacket) 45%, var(--jacket) 62%, var(--water) 80%, var(--water-dark) 100%);
  }
  .dots { left: 512px; top: 531px; display: flex; gap: 10px; }
  .dots i { width: 12px; height: 12px; border-radius: 50%; background: var(--white); display: block; }
  .dots i.off { background: #555; }

  .section-head {
    left: 85px; top: 587px; width: 941px; height: 40px; border: 1px solid #444;
    font-family: "Noto Serif", serif; font-weight: 700; font-size: 18px; color: var(--white);
    padding: 7px 0 0 21px;
  }

  .product-frame { width: 438px; height: 278px; border: 1px solid #555; top: 650px; }
  .product-shot { top: 11px; left: 12px; width: 412px; height: 253px; }
  .shot-dark { background: radial-gradient(ellipse at center, var(--tee-dark) 0%, #4a423a 45%, #e6e6e6 75%); }
  .shot-light { background: radial-gradient(ellipse at center, #fafafa 0%, #e9eceb 45%, #bdbdbd 80%), var(--teal); }
  .price-bar {
    top: 938px; width: 442px; height: 44px; background: var(--price-bg);
    font-family: "Noto Serif", serif; color: var(--ink);
  }
  .price-bar .name { left: 14px; top: 18px; font-size: 15px; }
  .price-bar .price { left: 285px; top: 11px; font-size: 15px; }
  .buy {
    left: 362px; top: 10px; width: 64px; height: 25px; background: var(--green);
    border: 1px solid var(--green-dark); color: var(--white); font-weight: 700; font-size: 15px;
    display: flex; align-items: center; justify-content: center;
  }
  .more {
    left: 773px; top: 1009px; width: 237px; height: 34px; background: var(--green);
    border: 1px solid var(--green-dark); color: var(--white); font-family: "Noto Serif", serif;
    font-weight: 700; font-size: 15px; display: flex; align-items: center;
  }
  .more .label { padding-left: 20px; width: 186px; }
  .more .arrow { height: 100%; border-left: 1px solid var(--green-dark); flex: 1; display: flex; align-items: center; justify-content: center; }

  .footer {
    left: 2px; top: 1078px; width: 1098px; height: 122px;
    background: linear-gradient(#353535, #242424);
  }
  .footer-cats { left: 86px; top: 1120px; font-size: 13px; color: var(--white); }
  .footer-cats span { margin-right: 34px; }
  .footer-links { left: 87px; top: 1150px; font-size: 12px; color: var(--white); }
  .footer-links b { font-weight: 400; margin: 0 8px; }
  .social-title { left: 793px; top: 1113px; font-size: 19px; font-weight: 600; color: var(--white); }
  .social-box { top: 1098px; width: 38px; height: 38px; background: #3b5db0; border: 2px solid #d8d8d8; }
  .copyright { left: 763px; top: 1167px; font-size: 11px; color: var(--white); }
</style>
</head>
<body>
<div class="page">
  <div class="abs util-bar"></div>
  <nav class="abs util-nav">HOME<span>|</span>JOIN EMAIL<span>|</span>CONTACT US<span>|</span>WISHLIST<span>|</span>LOGIN</nav>

  <div class="abs brand">BRISK TIDE</div>

  <div class="abs cart">
    <svg width="26" height="22" viewBox="0 0 26 22" aria-hidden="true">
      <path d="M1 2h4l3 11h13l3-8H7" fill="none" stroke="#fff" stroke-width="2"/>
      <circle cx="10" cy="18" r="2" fill="#fff"/><circle cx="19" cy="18" r="2" fill="#fff"/>
    </svg>
    <span>View cart &nbsp;|&nbsp; 0</span>
  </div>

  <nav class="abs main-nav"><a>SHIRTS</a><a>SHORTS</a><a>HEADWEAR</a></nav>
  <div class="abs checkout">Checkout</div>

  <div class="abs hero-band"></div>
  <div class="abs hero-photo" role="img" aria-label="Angler in a grey rain jacket holding a fly rod and a caught fish while standing in a river"></div>
  <div class="abs dots"><i></i><i></i><i></i><i class="off"></i></div>

  <div class="abs section-head">Featured Products</div>

  <div class="abs product-frame" style="left:92px">
    <div class="abs product-shot shot-dark" role="img" aria-label="Black tee shown from back and front with white brand print down the back"></div>
  </div>
  <div class="abs price-bar" style="left:91px">
    <span class="abs name">Black Tee</span><span class="abs price">$20.00</span><span class="abs buy">Buy</span>
  </div>

  <div class="abs product-frame" style="left:574px">
    <div class="abs product-shot shot-light" role="img" aria-label="White tee shown from back and front with a teal fish print on the back"></div>
  </div>
  <div class="abs price-bar" style="left:573px">
    <span class="abs name">White Tee</span><span class="abs price">$20.00</span><span class="abs buy">Buy</span>
  </div>

  <div class="abs more">
    <span class="label">View more products</span>
    <span class="arrow">
      <svg width="22" height="22" viewBox="0 0 22 22" aria-hidden="true">
        <circle cx="11" cy="11" r="10" fill="var(--green-deep)"/>
        <path d="M9 6l5 5-5 5" fill="none" stroke="#fff" stroke-width="2.5"/>
      </svg>
    </span>
  </div>

  <footer class="abs footer"></footer>
  <div class="abs footer-cats"><span>SHIRTS</span><span>SHORTS</span><span>HEADWEAR</span></div>
  <div class="abs footer-links">Home<b>|</b>Join email<b>|</b> Contact us<b>|</b> Wishlist<b>|</b> Login</div>
  <div class="abs social-title">Get Social</div>
  <div class="abs social-box" style="left:900px" role="img" aria-label="Social network link"></div>
  <div class="abs social-box" style="left:948px;background:#4aa3d8" role="img" aria-label="Social network link"></div>
  <div class="abs copyright">Copyright 2013 Brisk Tide. All rights reserved.</div>
</div>
</body>
</html>
```